A5 Flyer for Financial Services Business

I am after a re-design of our business flyer to fit in with our new branding style and logo colour scheme. Wanting something with a bit of designer flair that I could not create myself. I have included the flyer which I created which lacks style so dazzle me.

I want to use the same content.

Text for main body of flyer is

Are you a small business owner, tradie or KTAV Service Provider struggling to stay on top of your bookkeeping and compliance obligations? If so we would love to help you get back on track and take control of your business finances so that you can make informed business decisions and focus on what you do best.

We have over 20 years industry experience and, as a small business ourselves, we are able to offer our clients a personal bookkeeping solution tailored to meet the needs of your business.

Accounts Payable | Accounts Receivable
Customer Invoicing
Bank and Credit Card Reconciliations
Payroll | Superannuation | Payroll Tax
Business Activity | Instalment Activity Statements
Regular Financial Reports
Ledgr and TallyBooks Set-Up and Training

```html
<!DOCTYPE html>
<html lang="en">
<head>
<meta charset="utf-8">
<title>Even Keel Financial Services – Bookkeeping Flyer</title>
<link rel="stylesheet" href="https://fonts.googleapis.com/css2?family=Bebas+Neue&family=Oswald:wght@300&family=Raleway:wght@500;700;800&display=swap">
<style>
  :root {
    --backdrop: #c5e2e2;
    --paper: #f7f7f7;
    --teal: #21b1a7;
    --teal-deep: #15818a;
    --teal-text: #1ea59c;
    --ink: #2f2f2f;
    --white: #ffffff;
    --badge-ring: #9a9a9a;
  }
  html, body {
    margin: 0;
    padding: 0;
    width: 900px;
    height: 1200px;
    overflow: hidden;
    background: var(--backdrop);
  }
  .flyer {
    position: absolute;
    left: 40px;
    top: 20px;
    width: 820px;
    height: 1160px;
    background: var(--paper);
    overflow: hidden;
  }
  .flyer-shapes {
    position: absolute;
    inset: 0;
  }
  .brand {
    position: absolute;
    left: 0;
    top: 0;
    width: 398px;
    text-align: center;
    color: var(--teal-deep);
    font-family: "Raleway", sans-serif;
    font-weight: 500;
  }
  .brand-dot {
    width: 64px;
    height: 64px;
    border-radius: 50%;
    background: var(--teal-deep);
    margin: 18px auto 0;
  }
  .brand-name {
    font-size: 31px;
    letter-spacing: -0.5px;
    margin-top: 10px;
    line-height: 1;
  }
  .brand-tagline {
    font-size: 17px;
    letter-spacing: 6px;
    margin-top: 4px;
    line-height: 1;
  }
  .headline {
    position: absolute;
    left: 0;
    top: 222px;
    width: 398px;
    margin: 0;
    text-align: center;
    font-family: "Bebas Neue", sans-serif;
    font-weight: 400;
    font-size: 72px;
    line-height: 73px;
    color: var(--white);
  }
  .headline-rule {
    position: absolute;
    left: 150px;
    top: 527px;
    width: 95px;
    height: 3px;
    background: var(--white);
  }
  .intro {
    position: absolute;
    left: 52px;
    top: 600px;
    width: 398px;
    font-family: "Raleway", sans-serif;
    font-weight: 500;
    font-size: 19px;
    line-height: 28.5px;
    color: var(--ink);
    text-align: justify;
  }
  .intro p { margin: 0 0 14px; }
  .services {
    position: absolute;
    left: 497px;
    top: 606px;
    width: 300px;
    margin: 0;
    padding: 0;
    list-style: none;
    font-family: "Raleway", sans-serif;
    font-weight: 800;
    font-size: 17px;
    line-height: 21px;
    color: var(--teal-text);
  }
  .services li {
    display: flex;
    align-items: center;
    margin-bottom: 9.5px;
  }
  .tick {
    flex: none;
    width: 16px;
    height: 16px;
    margin-right: 15px;
  }
  .badge {
    position: absolute;
    left: 23px;
    top: 994px;
    width: 98px;
    height: 98px;
    border-radius: 50%;
    background: var(--white);
    box-sizing: border-box;
    border: 4px solid var(--badge-ring);
  }
  .bas-agent {
    position: absolute;
    left: 12px;
    top: 1096px;
    width: 120px;
    text-align: center;
    font-family: "Raleway", sans-serif;
    font-weight: 700;
    font-size: 13px;
    line-height: 16px;
    color: var(--white);
  }
  .credentials {
    position: absolute;
    left: 138px;
    top: 1059px;
    margin: 0;
    padding: 0;
    list-style: none;
    font-family: "Raleway", sans-serif;
    font-weight: 800;
    font-size: 19.5px;
    line-height: 27px;
    color: var(--white);
    white-space: nowrap;
  }
  .credentials li { display: flex; align-items: center; }
  .credentials .tick { width: 12px; height: 12px; margin-right: 5px; }
  .contact {
    position: absolute;
    left: 512px;
    top: 1050px;
    width: 300px;
    color: var(--white);
    white-space: nowrap;
  }
  .phone {
    display: flex;
    align-items: center;
    font-family: "Bebas Neue", sans-serif;
    font-size: 56px;
    line-height: 58px;
    letter-spacing: 0;
  }
  .phone-icon { width: 38px; height: 38px; margin-right: 9px; flex: none; }
  .website {
    font-family: "Oswald", sans-serif;
    font-weight: 300;
    font-size: 19px;
    line-height: 24px;
    margin-top: 0;
  }
</style>
</head>
<body>
<main class="flyer">
  <svg class="flyer-shapes" width="820" height="1160" viewBox="0 0 820 1160" aria-hidden="true">
    <defs>
      <linearGradient id="photo-tone" x1="0" y1="0" x2="1" y2="1">
        <stop offset="0" stop-color="#f6eedb"/>
        <stop offset="0.5" stop-color="#ece9e4"/>
        <stop offset="1" stop-color="#cfdde4"/>
      </linearGradient>
      <linearGradient id="swoosh" x1="0" y1="0" x2="1" y2="0">
        <stop offset="0" stop-color="#1c9ea0"/>
        <stop offset="1" stop-color="#0f6f7c"/>
      </linearGradient>
    </defs>
    <path d="M0 0 H398 V165 H65 A65 65 0 0 1 0 100 Z" fill="var(--paper)"/>
    <path d="M0 100 A65 65 0 0 0 65 165 H333 A65 65 0 0 1 398 230 V568 H60 A60 60 0 0 1 0 508 Z" fill="var(--teal)"/>
    <rect x="380" y="420" width="120" height="148" fill="var(--teal)"/>
    <rect x="700" y="540" width="120" height="140" fill="url(#swoosh)"/>
    <path d="M0 568 H730 A90 90 0 0 1 820 658 V1160 H0 Z" fill="var(--paper)"/>
    <rect x="0" y="1035" width="520" height="100" fill="var(--teal)"/>
    <path d="M380 1035 H820 V1160 H505 C490 1100 450 1050 380 1035 Z" fill="url(#swoosh)"/>
    <path d="M430 1035 H820 V1160 H530 C515 1100 490 1050 430 1035 Z" fill="var(--teal)"/>
  </svg>

  <svg role="img" aria-label="Photo of a person working with a calculator, notebook and glasses at a bright office desk" style="position:absolute;left:398px;top:0" width="422" height="568" viewBox="0 0 422 568">
    <path d="M0 0 H422 V568 H60 A60 60 0 0 1 0 508 Z" fill="url(#photo-tone)"/>
  </svg>

  <header class="brand">
    <div class="brand-dot"></div>
    <div class="brand-name">EVEN KEEL</div>
    <div class="brand-tagline">Financial Services</div>
  </header>

  <h1 class="headline">Bookkeeping<br>Tailored to<br>Your Business<br>Needs</h1>
  <div class="headline-rule"></div>

  <section class="intro">
    <p>Are you a small business owner, tradie or KTAV Service Provider struggling to stay on top of your bookkeeping and compliance obligations? If so we would love to help you get back on track and take control of your business finances so that you can make informed business decisions and focus on what you do best.</p>
    <p>We have over 20 years industry experience and, as a small business ourselves, we are able to offer our clients a personal bookkeeping solution tailored to meet the needs of your business.</p>
  </section>

  <ul class="services">
    <li><svg class="tick" viewBox="0 0 16 16"><rect x="1" y="3" width="12" height="12" fill="none" stroke="currentColor" stroke-width="2"/><path d="M4 8 L7 11 L15 2" fill="none" stroke="currentColor" stroke-width="2.4"/></svg>ACCOUNTS PAYABLE</li>
    <li><svg class="tick" viewBox="0 0 16 16"><rect x="1" y="3" width="12" height="12" fill="none" stroke="currentColor" stroke-width="2"/><path d="M4 8 L7 11 L15 2" fill="none" stroke="currentColor" stroke-width="2.4"/></svg>ACCOUNTS RECEIVABLE</li>
    <li><svg class="tick" viewBox="0 0 16 16"><rect x="1" y="3" width="12" height="12" fill="none" stroke="currentColor" stroke-width="2"/><path d="M4 8 L7 11 L15 2" fill="none" stroke="currentColor" stroke-width="2.4"/></svg>CUSTOMER INVOICING</li>
    <li><svg class="tick" viewBox="0 0 16 16"><rect x="1" y="3" width="12" height="12" fill="none" stroke="currentColor" stroke-width="2"/><path d="M4 8 L7 11 L15 2" fill="none" stroke="currentColor" stroke-width="2.4"/></svg>BANK AND CREDIT CARD<br>RECONCILIATIONS</li>
    <li><svg class="tick" viewBox="0 0 16 16"><rect x="1" y="3" width="12" height="12" fill="none" stroke="currentColor" stroke-width="2"/><path d="M4 8 L7 11 L15 2" fill="none" stroke="currentColor" stroke-width="2.4"/></svg>PAYROLL</li>
    <li><svg class="tick" viewBox="0 0 16 16"><rect x="1" y="3" width="12" height="12" fill="none" stroke="currentColor" stroke-width="2"/><path d="M4 8 L7 11 L15 2" fill="none" stroke="currentColor" stroke-width="2.4"/></svg>SUPERANNUATION</li>
    <li><svg class="tick" viewBox="0 0 16 16"><rect x="1" y="3" width="12" height="12" fill="none" stroke="currentColor" stroke-width="2"/><path d="M4 8 L7 11 L15 2" fill="none" stroke="currentColor" stroke-width="2.4"/></svg>PAYROLL TAX</li>
    <li><svg class="tick" viewBox="0 0 16 16"><rect x="1" y="3" width="12" height="12" fill="none" stroke="currentColor" stroke-width="2"/><path d="M4 8 L7 11 L15 2" fill="none" stroke="currentColor" stroke-width="2.4"/></svg>BUSINESS ACTIVITY</li>
    <li><svg class="tick" viewBox="0 0 16 16"><rect x="1" y="3" width="12" height="12" fill="none" stroke="currentColor" stroke-width="2"/><path d="M4 8 L7 11 L15 2" fill="none" stroke="currentColor" stroke-width="2.4"/></svg>INSTALMENT ACTIVITY<br>STATEMENTS</li>
    <li><svg class="tick" viewBox="0 0 16 16"><rect x="1" y="3" width="12" height="12" fill="none" stroke="currentColor" stroke-width="2"/><path d="M4 8 L7 11 L15 2" fill="none" stroke="currentColor" stroke-width="2.4"/></svg>REGULAR FINANCIAL<br>REPORTS</li>
    <li><svg class="tick" viewBox="0 0 16 16"><rect x="1" y="3" width="12" height="12" fill="none" stroke="currentColor" stroke-width="2"/><path d="M4 8 L7 11 L15 2" fill="none" stroke="currentColor" stroke-width="2.4"/></svg>LEDGR AND TALLYBOOKS<br>SET-UP AND TRAINING</li>
  </ul>

  <footer>
    <div class="badge" role="img" aria-label="Registered agent badge"></div>
    <div class="bas-agent">BAS Agent<br>12345678</div>
    <ul class="credentials">
      <li><svg class="tick" viewBox="0 0 16 16"><rect x="1" y="3" width="12" height="12" fill="none" stroke="currentColor" stroke-width="2"/><path d="M4 8 L7 11 L15 2" fill="none" stroke="currentColor" stroke-width="2.4"/></svg>LEDGR CERTIFIED ADVISOR</li>
      <li><svg class="tick" viewBox="0 0 16 16"><rect x="1" y="3" width="12" height="12" fill="none" stroke="currentColor" stroke-width="2"/><path d="M4 8 L7 11 L15 2" fill="none" stroke="currentColor" stroke-width="2.4"/></svg>TALLYBOOKS PROADVISOR</li>
    </ul>
    <div class="contact">
      <div class="phone">
        <svg class="phone-icon" viewBox="0 0 40 40" aria-hidden="true">
          <rect x="1" y="1" width="38" height="38" rx="9" fill="var(--white)"/>
          <path d="M13 9 L17 9 L19 15 L16 17 C17.5 21 19.5 23 23 24.5 L25 21.5 L31 23.5 L31 27.5 C31 29.5 29.5 31 27.5 31 C18 30.5 9.5 22 9 12.5 C9 10.5 11 9 13 9 Z" fill="var(--teal-deep)"/>
          <path d="M22 9 A9 9 0 0 1 31 18 M22 13 A5 5 0 0 1 27 18" fill="none" stroke="var(--teal-deep)" stroke-width="2"/>
        </svg>
        <span>0400 123 456</span>
      </div>
      <div class="website">evenkeelfinancialservices.com.au</div>
    </div>
  </footer>
</main>
</body>
</html>
```